diesel mechanic business card design

stalwart diesel is a new and upcoming business we are looking for some bad ass designs to help get us started we offer 24 hour road service, off road recovery, welding and custom fabrications we are diesel mechanics so our design should be bold and eye catching flames wrenches engine parts are cool we work in an industrial environment around heavy trucks and equipment this in not a quikko slick we fix it all nothing is to big or to small the colors red and black are always a plus but we are open to anything you guys can come up with ready set go

Target Market(s)

other small business primarily trucking and transportation companys

Industry/Entity Type

Business

Contact Information for Business Card

company name Stalwert diesel truck & trailer repair / address 14 rear north benton ave harwick OH 44610 / ownersAdam DeLuccie 570-614-3385 / Curtis Vanholm 570-248-7731 E mail owenmarcotti@fieldpost.example fax 570-692-1856

Requirements
Nice to have
• industrial modern design
Should not have
• rainbows butterfly's unicorns or cupcakes

```html
<!DOCTYPE html>
<html lang="en">
<head>
<meta charset="utf-8">
<title>Stalwert Diesel – Business Card</title>
<link rel="stylesheet" href="https://fonts.googleapis.com/css2?family=Exo+2:wght@600;700&family=Open+Sans:wght@400;600&display=swap">
<style>
  :root {
    --page-bg: #e9e6e1;
    --brand-blue: #4b5cc9;
    --brand-blue-deep: #3f4fb8;
    --card-white: #ffffff;
    --ink: #151515;
    --on-blue: #ffffff;
  }
  html, body {
    margin: 0;
    padding: 0;
    width: 1200px;
    height: 885px;
    overflow: hidden;
    background: var(--page-bg);
  }
  .canvas {
    position: relative;
    width: 1200px;
    height: 885px;
  }
  .card {
    position: absolute;
    overflow: hidden;
    box-shadow: 0 10px 28px rgba(0,0,0,0.18);
  }

  /* Front (portrait) */
  .card-front {
    left: 60px;
    top: 110px;
    width: 380px;
    height: 665px;
    background: var(--card-white);
  }
  .front-band {
    position: absolute;
    left: 0;
    top: 0;
    width: 58px;
    height: 100%;
    background: var(--brand-blue);
  }
  .front-step {
    position: absolute;
    background: var(--brand-blue);
  }
  .front-step.upper { left: 0; top: 330px; width: 128px; height: 62px; }
  .front-step.lower { left: 0; top: 452px; width: 98px; height: 52px; }

  .front-brand {
    position: absolute;
    left: 100px;
    right: 24px;
    top: 160px;
    display: flex;
    align-items: center;
    gap: 12px;
  }
  .brand-square {
    flex: none;
    width: 22px;
    height: 22px;
    background: var(--brand-blue);
  }
  .brand-name {
    font-family: "Exo 2", sans-serif;
    font-weight: 700;
    color: var(--brand-blue);
    margin: 0;
    line-height: 1.05;
    white-space: nowrap;
  }
  .brand-tagline {
    display: block;
    font-size: 11px;
    letter-spacing: 0.06em;
    text-transform: uppercase;
    margin-top: 6px;
  }
  .front-brand .brand-name { font-size: 40px; }

  .contact-person {
    position: absolute;
    left: 150px;
    margin: 0;
    white-space: nowrap;
  }
  .contact-person.owner-one { top: 336px; }
  .contact-person.owner-two { top: 458px; left: 118px; }
  .person-name {
    display: block;
    font-family: "Exo 2", sans-serif;
    font-weight: 700;
    font-size: 28px;
    color: var(--brand-blue);
    line-height: 1.05;
  }
  .person-phone {
    display: block;
    font-family: "Open Sans", sans-serif;
    font-weight: 400;
    font-size: 24px;
    color: var(--ink);
    line-height: 1.2;
  }

  /* Back (landscape) */
  .card-back {
    left: 490px;
    top: 252px;
    width: 665px;
    height: 380px;
    background: linear-gradient(160deg, var(--brand-blue-deep) 0%, var(--brand-blue) 55%, #5a6bd4 100%);
    color: var(--on-blue);
  }
  .back-brand {
    position: absolute;
    right: 48px;
    top: 70px;
    width: 320px;
    display: flex;
    align-items: center;
    gap: 12px;
  }
  .back-brand .brand-square { background: var(--on-blue); }
  .back-brand .brand-name {
    color: var(--on-blue);
    font-size: 40px;
  }
  .back-brand .brand-tagline { font-size: 12px; }
  .back-contact {
    position: absolute;
    left: 48px;
    bottom: 52px;
    margin: 0;
    padding: 0;
    list-style: none;
    font-family: "Open Sans", sans-serif;
    font-weight: 400;
    font-size: 19px;
    line-height: 1.6;
    white-space: nowrap;
  }
</style>
</head>
<body>
<main class="canvas">

  <section class="card card-front" aria-label="Business card front">
    <div class="front-band"></div>
    <div class="front-step upper"></div>
    <div class="front-step lower"></div>

    <div class="front-brand">
      <span class="brand-square"></span>
      <h1 class="brand-name">STALWERT<span class="brand-tagline">diesel truck &amp; trailer repair</span></h1>
    </div>

    <p class="contact-person owner-one">
      <span class="person-name">Owen Marcotti</span>
      <span class="person-phone">570-614-3385</span>
    </p>
    <p class="contact-person owner-two">
      <span class="person-name">Curtis Vanholm</span>
      <span class="person-phone">570-248-7731</span>
    </p>
  </section>

  <section class="card card-back" aria-label="Business card back">
    <div class="back-brand">
      <span class="brand-square"></span>
      <h2 class="brand-name">STALWERT<span class="brand-tagline">diesel truck &amp; trailer repair</span></h2>
    </div>
    <ul class="back-contact">
      <li>fax: 570-692-1856</li>
      <li>owenmarcotti@fieldpost.example</li>
      <li>14 rear north benton ave harwick OH 44610</li>
    </ul>
  </section>

</main>
</body>
</html>
```